New York City Sponsorship Page with Click Through Supporting Pages

Metro Workforce Guild, the leading New York City resource for HR Professionals is a membership organization with almost 2,000 individual members.

We need section/page(s) created for our current sponsorship offerings. Our platform is on ClubRoster Platform and we need capability to edit the page, etc. It must be HTML ready/coded.

Attached is the mock up of how we want the page to look (pages mockup pdf) as well as each of the categories which should be included (in the excel files). Our current page is here: http://www.metroworkguild.org/?page=sponsors and is not easy to read through. We want something that is visually appealing and clean but showcases all of the different ways to sponsor the Chapter.

Additionally, we are taking the information from this page and turning it into a brochure.

Target Market(s)

New York City Companies who have HR Professionals or services they want to attract or offer.

Coding

Coded - Design and coding required

Number of Pages Required

5+ page

Requirements
Must have
• Clean Look and feel, easy functionality, necessary information and purchases. Match the top navigation of current page. Opportunity for current sponsor logos to be highlighted on the page. Easy to update/maintain.
Nice to have
• Option to pay for sponsorships through the page using our credit card processor.
Should not have
• Overwhelming text in sections

```html
<!DOCTYPE html>
<html lang="en">
<head>
<meta charset="utf-8">
<title>Metro Workforce Guild – Sponsorship Opportunities</title>
<link href="https://fonts.googleapis.com/css2?family=Fira+Sans:wght@400;500;600;700&family=Open+Sans:wght@400;600;700&family=Roboto+Condensed:wght@400;700&display=swap" rel="stylesheet">
<style>
:root{
  --navy:#0a2842;
  --navy-dark:#072036;
  --blue:#1a7fd0;
  --programs:#1677c4;
  --red:#c3080e;
  --charcoal:#2b2d31;
  --slate:#153a59;
  --text:#1c1c1c;
  --link:#2a78c1;
  --frame:#e6e6e6;
  --light:#f2f2f2;
  --white:#ffffff;
}
*{box-sizing:border-box;margin:0;padding:0}
html,body{width:843px;height:1200px;overflow:hidden}
body{background:var(--frame);font-family:"Open Sans",sans-serif;color:var(--text);position:relative}
.page{position:absolute;left:10px;top:9px;width:823px;height:1183px;background:var(--white);overflow:hidden}
.abs{position:absolute}

/* utility bar */
.utility{left:0;top:0;width:823px;height:22px;background:var(--navy);display:flex;align-items:center;justify-content:flex-end;padding-right:55px;gap:9px;font:700 7px "Open Sans",sans-serif;color:var(--white)}
.utility .search{width:98px;height:13px;background:var(--white);border-radius:1px;font:400 6.5px "Open Sans",sans-serif;color:#999;padding:3px 4px;margin-left:4px}
.social{display:flex;gap:4px}
.social span{width:13px;height:13px;background:var(--link);display:block}

/* header */
.header{left:0;top:22px;width:823px;height:53px;background:var(--white)}
.brand{position:absolute;left:60px;top:15px;display:flex;align-items:center;gap:5px;font:700 13px "Roboto Condensed",sans-serif;color:var(--red)}
.brand i{width:14px;height:14px;border-radius:50%;background:var(--navy);display:block}
.nav{position:absolute;right:68px;top:19px;display:flex;gap:21px;font:400 11px "Roboto Condensed",sans-serif;color:var(--link)}

.hero{left:0;top:75px;width:823px;height:95px;background:linear-gradient(180deg,#0b1726 0%,#1d2a3c 55%,#3a3a3c 100%)}

.crumb{left:24px;top:178px;font:600 7px "Open Sans",sans-serif;color:var(--text)}

.title-row{left:134px;top:218px;width:556px;display:flex;align-items:center;gap:14px}
.title-row .rule{flex:1;height:1px;background:#cfcfcf}
.title-row h1{font:600 18px "Fira Sans",sans-serif;color:var(--slate);white-space:nowrap}
.accent{color:var(--red)}
.intro{left:0;width:823px;text-align:center;font:600 8.5px "Open Sans",sans-serif}

/* categories */
.cats{left:0;top:351px;width:823px;height:292px;background:linear-gradient(135deg,#0c5fa8 0%,#1a86d6 45%,#39b0ef 100%)}
.cats h2{position:absolute;left:0;top:50px;width:823px;text-align:center;font:600 14px "Fira Sans",sans-serif;color:var(--white)}
.cats .hr{position:absolute;top:60px;height:1px;width:64px;background:rgba(255,255,255,.6)}
.cards{position:absolute;left:54px;top:110px;width:714px;height:130px;border:2px solid var(--white);border-radius:7px;display:flex;overflow:hidden}
.card{flex:1;position:relative;color:var(--white);text-align:center}
.card.strategic{background:var(--slate)}
.card.programs{background:var(--programs)}
.card.advert{background:var(--red)}
.card.custom{background:var(--charcoal)}
.card h3{position:absolute;left:56px;right:8px;top:12px;text-align:left;font:600 11.5px/1.2 "Fira Sans",sans-serif}
.card.strategic h3{left:0;right:0;text-align:center;padding-left:8px}
.card p{position:absolute;left:22px;right:22px;top:52px;font:400 8.6px/1.4 "Open Sans",sans-serif}
.badge{position:absolute;top:442px;width:58px;height:58px;border-radius:50%;border:2px solid var(--white);display:flex;align-items:center;justify-content:center}
.price{position:absolute;top:578px;width:104px;height:27px;border:1.5px solid var(--white);border-radius:4px;display:flex;align-items:center;justify-content:center;font:700 13px "Fira Sans",sans-serif;color:var(--white)}

/* actions */
.actions{left:0;top:643px;width:823px;height:178px;background:var(--light)}
.action{position:absolute;top:54px;height:35px;border-radius:0 5px 5px 0;padding-left:30px;display:flex;align-items:center;justify-content:center;color:var(--white);font:600 10px/1.25 "Fira Sans",sans-serif;text-align:center}
.action-icon{position:absolute;top:39px;width:64px;height:64px;border-radius:50%;border:3px solid var(--white);box-shadow:0 0 0 1px #d4d4d4;display:flex;align-items:center;justify-content:center}

/* sponsors */
.thanks{left:252px;top:832px;width:318px;display:flex;align-items:center;gap:14px}
.thanks .rule{flex:1;height:1px;background:#bfbfbf}
.thanks h2{font:600 13px "Fira Sans",sans-serif;color:var(--slate);white-space:nowrap}
.tier{font:600 12.5px "Fira Sans",sans-serif;color:#333;top:884px}
.sponsor{top:912px;font:600 17px "Fira Sans",sans-serif;display:flex;align-items:center;gap:6px}
.sponsor i{display:block;width:10px;height:10px}

/* footer */
.footer{left:0;top:987px;width:823px;height:196px;background:var(--navy)}
.footer h4{position:absolute;top:29px;font:400 14px "Roboto Condensed",sans-serif;color:var(--white)}
.footer ul{position:absolute;top:56px;list-style:none;font:400 8px/14.5px "Open Sans",sans-serif;color:var(--white)}
.contact p{font:400 8px "Open Sans",sans-serif;color:var(--white);margin-bottom:11px}
.affiliate{position:absolute;left:353px;top:22px;width:143px;height:104px;background:var(--white);padding:9px}
.affiliate div{width:100%;height:100%;background:#4d6fa6}
.f-social{position:absolute;left:553px;top:60px;display:flex;gap:7px}
.f-social span{width:22px;height:22px;background:var(--link);display:block}
.legal{position:absolute;left:0;bottom:0;width:823px;height:28px;background:var(--navy-dark);text-align:center;font:600 7px/28px "Open Sans",sans-serif;color:var(--white)}
</style>
</head>
<body>
<div class="page">

  <div class="abs utility">
    <span>CONTACT US</span><span>SIGN IN</span><span>JOIN/RENEW</span>
    <span class="search">Enter search criteria...</span>
    <span class="social"><span></span><span></span><span></span><span></span><span></span></span>
  </div>

  <header class="abs header">
    <div class="brand"><i></i>Metro Workforce Guild</div>
    <nav class="nav">
      <span>Our New Website</span><span>About Us</span><span>Membership</span><span>Events</span><span>Sponsorships</span><span>Career Center</span><span>HR Resources</span>
    </nav>
  </header>

  <div class="abs hero" role="img" aria-label="Night skyline of Manhattan with lit office towers"></div>

  <div class="abs crumb">SPONSORSHIPS &gt; SPONSORSHIP OPPORTUNITIES</div>

  <div class="abs title-row">
    <span class="rule"></span>
    <h1>INVITATION FOR <span class="accent">SPONSORS</span></h1>
    <span class="rule"></span>
  </div>
  <p class="abs intro" style="top:276px">Thank you for your interest in Metro Workforce Guild.</p>
  <p class="abs intro" style="top:304px">As a premier HR chapter, we offer many opportunities to increase your exposure to the New York City HR community.</p>

  <section class="abs cats">
    <span class="hr" style="left:119px"></span>
    <h2>Choose the sponsorship category that best meets your needs:</h2>
    <span class="hr" style="left:640px"></span>
    <div class="cards">
      <div class="card strategic"><h3>Strategic<br>Partnership</h3><p>Opportunities for a strategic sponsorship at different levels, each providing a valuable set of great benefits.</p></div>
      <div class="card programs"><h3>Programs /<br>Events</h3><p>Opportunities to sponsor a wide range of events like all-day conference, 2 hour sessions etc.</p></div>
      <div class="card advert"><h3>Advertising /<br>Promotion</h3><p>Opportunities for regular orone time digital sponsoring in form of website banners, website ads, e-blasts etc.</p></div>
      <div class="card custom"><h3>Custom</h3><p>Build your own sponsorship program from our variety of opportunities.</p></div>
    </div>
  </section>

  <div class="badge" style="left:41px;background:var(--slate)"><svg width="30" height="30" viewBox="0 0 30 30" fill="#fff"><circle cx="9" cy="7" r="3"/><circle cx="21" cy="7" r="3"/><rect x="6" y="11" width="6" height="12" rx="2"/><rect x="18" y="11" width="6" height="12" rx="2"/><rect x="11" y="12" width="8" height="2"/></svg></div>
  <div class="badge" style="left:220px;background:var(--programs)"><svg width="30" height="30" viewBox="0 0 30 30" fill="#fff"><circle cx="9" cy="11" r="2.5"/><circle cx="15" cy="9" r="2.5"/><circle cx="21" cy="11" r="2.5"/><path d="M3 22 L9 14 L15 12 L21 14 L27 22Z"/></svg></div>
  <div class="badge" style="left:399px;background:var(--red)"><svg width="30" height="30" viewBox="0 0 30 30" fill="none" stroke="#fff" stroke-width="2"><path d="M5 12h5l10-6v18l-10-6H5z"/><path d="M8 18l2 6"/><path d="M24 11l3-2M24 15h4M24 19l3 2"/></svg></div>
  <div class="badge" style="left:577px;background:var(--charcoal)"><svg width="30" height="30" viewBox="0 0 30 30" fill="#fff"><rect x="4" y="17" width="22" height="4"/><rect x="4" y="23" width="22" height="3"/><rect x="4" y="8" width="8" height="6"/><path d="M20 4l4 5h-3v6h-2V9h-3z"/></svg></div>

  <div class="price" style="left:92px;background:var(--slate)">$3,500+</div>
  <div class="price" style="left:271px;background:var(--programs)">$500+</div>
  <div class="price" style="left:449px;background:var(--red)">$150+</div>
  <div class="price" style="left:627px;background:var(--charcoal)">$250+</div>

  <section class="abs actions">
    <div class="action" style="left:126px;width:164px;background:var(--slate)">More about our<br>sponsorship packages</div>
    <div class="action-icon" style="left:86px;background:var(--slate)"><svg width="34" height="34" viewBox="0 0 34 34" fill="none" stroke="#fff" stroke-width="2"><rect x="4" y="8" width="26" height="18" rx="2"/><path d="M4 9l13 10 13-10"/></svg></div>
    <div class="action" style="left:350px;width:164px;background:var(--blue)">Book your<br>sponsorship packages</div>
    <div class="action-icon" style="left:310px;background:var(--blue)"><svg width="34" height="34" viewBox="0 0 34 34" fill="none" stroke="#fff" stroke-width="2.5"><circle cx="15" cy="19" r="11"/><circle cx="15" cy="19" r="5"/><path d="M15 19L29 5M24 5h5v5"/></svg></div>
    <div class="action" style="left:574px;width:164px;background:var(--red)">Contact our<br>sponsorship team</div>
    <div class="action-icon" style="left:534px;background:var(--red)"><svg width="34" height="34" viewBox="0 0 34 34" fill="none" stroke="#fff" stroke-width="2.2"><path d="M9 5l5 6-3 3c2 4 5 7 9 9l3-3 6 5-3 4C15 29 5 19 5 8z"/><path d="M20 8a7 7 0 0 1 6 6M20 3a12 12 0 0 1 11 11"/></svg></div>
  </section>

  <div class="abs thanks"><span class="rule"></span><h2>Thanks to <span class="accent">our sponsors</span></h2><span class="rule"></span></div>
  <div class="abs tier" style="left:82px">Gold</div>
  <div class="abs tier" style="left:433px">Silver</div>
  <div class="abs sponsor" style="left:82px;color:var(--slate)">Harlow Brant</div>
  <div class="abs sponsor" style="left:236px;color:#232a6b">Transit Perks Group</div>
  <div class="abs sponsor" style="left:431px;color:#222"><i style="background:#1e8a3a"></i>Beacon Benefits</div>
  <div class="abs sponsor" style="left:613px;color:#2a6fb7">Staffwell</div>

  <footer class="abs footer">
    <h4 style="left:82px">Navigation</h4>
    <ul style="left:82px"><li>About Us</li><li>Membership</li><li>Events</li><li>Career Center</li><li>Sponsorships</li><li>HR Resources</li></ul>
    <h4 style="left:209px">Contact Us</h4>
    <div class="contact" style="position:absolute;left:209px;top:56px">
      <p>Phone: 212-555-0147</p><p>Fax: 212-555-0162</p><p>info@metroworkguild.org</p>
    </div>
    <div class="affiliate"><div role="img" aria-label="Affiliate badge"></div></div>
    <h4 style="left:553px">Connect With Us</h4>
    <div class="f-social"><span></span><span></span><span></span><span></span><span></span></div>
    <div class="legal">Membership Software Powered by ClubRoster &nbsp;::&nbsp; Legal</div>
  </footer>

</div>
</body>
</html>
```